Business Card Design needed for logo design project

Our business needs a business card design. I'm not sure what format files are generally delivered back, but clearly I will need the ability to edit to add colleagues contact details.

Our logo is attached.

Brivanor is a 3D design services company, providing app, serious/educational game, VR and AR websites/applications to corporate clients.

Target Market(s)

Corporate blue-chip clients needing 3D design services

Industry/Entity Type

Business

Font styles to use
Sans Serif

Requirements
Must have
• Templated such that I can add details (name, phone number etc). Needs to include logo from previous project winner - attached.

```html
<!DOCTYPE html>
<html lang="en">
<head>
<meta charset="utf-8">
<title>Brivanor Business Cards</title>
<link rel="stylesheet" href="https://fonts.googleapis.com/css2?family=Exo+2:wght@400;500;600;700&display=swap">
<style>
  :root {
    --backdrop: #e3e3e3;
    --card-red: #d51f2a;
    --card-red-light: #e41f2c;
    --card-red-deep: #be1c25;
    --arc-shade: rgba(120, 10, 18, 0.18);
    --band-dark: #9d1820;
    --icon-dark: #8c141b;
    --ink-light: #ffffff;
    --card-w: 438px;
    --card-h: 263px;
  }
  * { box-sizing: border-box; margin: 0; padding: 0; }
  html, body {
    width: 1200px; height: 817px; overflow: hidden;
    background: var(--backdrop);
    font-family: "Exo 2", sans-serif;
  }
  .sheet { position: relative; width: 1200px; height: 817px; }
  .card {
    position: absolute;
    width: var(--card-w); height: var(--card-h);
    background: linear-gradient(200deg, var(--card-red-light) 0%, var(--card-red) 50%, var(--card-red-deep) 100%);
    overflow: hidden;
    color: var(--ink-light);
    box-shadow: 0 4px 8px rgba(0,0,0,0.12);
  }
  .card--front-top { left: 122px; top: 101px; }
  .card--back-top  { left: 638px; top: 101px; }
  .card--front-bottom { left: 122px; top: 438px; }
  .card--back-bottom  { left: 638px; top: 438px; }
  .card__arcs { position: absolute; inset: 0; width: 100%; height: 100%; }

  .brand { position: absolute; display: flex; align-items: center; }
  .brand__dot { border-radius: 50%; background: var(--ink-light); flex: none; }
  .brand__name { font-weight: 500; letter-spacing: 0.04em; line-height: 1; text-transform: uppercase; }

  .brand--front { left: 30px; top: 24px; gap: 5px; }
  .brand--front .brand__dot { width: 31px; height: 31px; }
  .brand--front .brand__name { font-size: 21px; }

  .brand--back { left: 97px; top: 107px; gap: 8px; }
  .brand--back .brand__dot { width: 53px; height: 53px; }
  .brand--back .brand__name { font-size: 38px; }

  .person { position: absolute; left: 240px; top: 99px; width: 120px; text-align: center; }
  .person__name { font-size: 17px; font-weight: 600; line-height: 1; white-space: nowrap; margin-left: -20px; margin-right: -20px; }
  .person__title { font-size: 7px; letter-spacing: 0.06em; margin-top: 2px; }

  .contacts { position: absolute; left: 203px; top: 162px; list-style: none; }
  .contacts__item { display: flex; align-items: center; height: 17px; font-size: 7.4px; letter-spacing: 0.02em; }
  .contacts__icon { width: 10px; height: 10px; margin-right: 12px; fill: var(--icon-dark); flex: none; }

  .web-band { position: absolute; left: 0; bottom: 0; width: 180px; height: 13px; }
  .web-band svg { position: absolute; inset: 0; }
  .web-band__text { position: absolute; left: 29px; top: 2px; font-size: 6.8px; letter-spacing: 0.22em; }
</style>
</head>
<body>
<main class="sheet">

  <!-- Front, top -->
  <section class="card card--front-top">
    <svg class="card__arcs" viewBox="0 0 438 263" aria-hidden="true">
      <path d="M10 0 C 120 40, 100 200, 60 263" fill="none" stroke="var(--arc-shade)" stroke-width="14"/>
      <circle cx="390" cy="160" r="130" fill="none" stroke="var(--arc-shade)" stroke-width="22"/>
      <path d="M438 20 C 380 60, 370 200, 438 263 Z" fill="var(--arc-shade)"/>
    </svg>
    <div class="brand brand--front"><span class="brand__dot"></span><span class="brand__name">Brivanor</span></div>
    <div class="person">
      <p class="person__name">Your Name Here</p>
      <p class="person__title">Your Job Title</p>
    </div>
    <ul class="contacts">
      <li class="contacts__item"><svg class="contacts__icon" viewBox="0 0 10 10"><path d="M5 0a3.4 3.4 0 0 0-3.4 3.4C1.6 6 5 10 5 10s3.4-4 3.4-6.6A3.4 3.4 0 0 0 5 0zm0 4.8a1.4 1.4 0 1 1 0-2.8 1.4 1.4 0 0 1 0 2.8z"/></svg>24 - 30 your address no. 12, Riverton. RV 20417</li>
      <li class="contacts__item"><svg class="contacts__icon" viewBox="0 0 10 10"><path d="M2 1l2 2-1 1.3c.6 1.2 1.5 2.1 2.7 2.7L7 6l2 2-1.2 1.5C4.5 9.3.7 5.5.5 2.2z"/></svg>555 018 2740</li>
      <li class="contacts__item"><svg class="contacts__icon" viewBox="0 0 10 10"><path d="M2.5 0h5v3h-5zM0 3.5h10v4.5H8V10H2V8H0zM3 7v2h4V7z"/></svg>555 018 2793</li>
      <li class="contacts__item"><svg class="contacts__icon" viewBox="0 0 10 10"><path d="M0 1.5h10v7H0zM1 2.5l4 3 4-3z"/></svg>your@emailhere.com</li>
    </ul>
    <div class="web-band">
      <svg viewBox="0 0 180 13" preserveAspectRatio="none"><path d="M0 0H168L180 13H0Z" fill="var(--band-dark)"/></svg>
      <span class="web-band__text">www.yourwebsite.com</span>
    </div>
  </section>

  <!-- Back, top -->
  <section class="card card--back-top">
    <svg class="card__arcs" viewBox="0 0 438 263" aria-hidden="true">
      <circle cx="40" cy="130" r="150" fill="none" stroke="var(--arc-shade)" stroke-width="20"/>
      <path d="M0 80 C 60 120, 120 240, 120 263 H0Z" fill="var(--arc-shade)"/>
    </svg>
    <div class="brand brand--back"><span class="brand__dot"></span><span class="brand__name">Brivanor</span></div>
  </section>

  <!-- Front, bottom -->
  <section class="card card--front-bottom">
    <svg class="card__arcs" viewBox="0 0 438 263" aria-hidden="true">
      <path d="M10 0 C 120 40, 100 200, 60 263" fill="none" stroke="var(--arc-shade)" stroke-width="14"/>
      <circle cx="390" cy="160" r="130" fill="none" stroke="var(--arc-shade)" stroke-width="22"/>
      <path d="M438 20 C 380 60, 370 200, 438 263 Z" fill="var(--arc-shade)"/>
    </svg>
    <div class="brand brand--front"><span class="brand__dot"></span><span class="brand__name">Brivanor</span></div>
    <div class="person">
      <p class="person__name">Your Name Here</p>
      <p class="person__title">Your Job Title</p>
    </div>
    <ul class="contacts">
      <li class="contacts__item"><svg class="contacts__icon" viewBox="0 0 10 10"><path d="M5 0a3.4 3.4 0 0 0-3.4 3.4C1.6 6 5 10 5 10s3.4-4 3.4-6.6A3.4 3.4 0 0 0 5 0zm0 4.8a1.4 1.4 0 1 1 0-2.8 1.4 1.4 0 0 1 0 2.8z"/></svg>24 - 30 your address no. 12, Riverton. RV 20417</li>
      <li class="contacts__item"><svg class="contacts__icon" viewBox="0 0 10 10"><path d="M2 1l2 2-1 1.3c.6 1.2 1.5 2.1 2.7 2.7L7 6l2 2-1.2 1.5C4.5 9.3.7 5.5.5 2.2z"/></svg>555 018 2740</li>
      <li class="contacts__item"><svg class="contacts__icon" viewBox="0 0 10 10"><path d="M2.5 0h5v3h-5zM0 3.5h10v4.5H8V10H2V8H0zM3 7v2h4V7z"/></svg>555 018 2793</li>
      <li class="contacts__item"><svg class="contacts__icon" viewBox="0 0 10 10"><path d="M0 1.5h10v7H0zM1 2.5l4 3 4-3z"/></svg>your@emailhere.com</li>
    </ul>
    <div class="web-band">
      <svg viewBox="0 0 180 13" preserveAspectRatio="none"><path d="M0 0H168L180 13H0Z" fill="var(--band-dark)"/></svg>
      <span class="web-band__text">www.yourwebsite.com</span>
    </div>
  </section>

  <!-- Back, bottom -->
  <section class="card card--back-bottom">
    <svg class="card__arcs" viewBox="0 0 438 263" aria-hidden="true">
      <circle cx="40" cy="130" r="150" fill="none" stroke="var(--arc-shade)" stroke-width="20"/>
      <path d="M0 80 C 60 120, 120 240, 120 263 H0Z" fill="var(--arc-shade)"/>
    </svg>
    <div class="brand brand--back"><span class="brand__dot"></span><span class="brand__name">Brivanor</span></div>
  </section>

</main>
</body>
</html>
```